Need Bus charter business website,

I am starting a bus charter business in the near future. I am based in Geelong, Victoria in Australia. I will have a 25 or 28 seater bus that will be used to take people on charted trips. Whether they be to birthday parties, weddings, sporting events, corporate events, mystery trips, going down the Great Ocean Road, or anywhere someone wants. As for colour scheme, I'm leaning towards something blue and grey, but open to anything really that catches my eye. I played around with a basic web design program and made a basic site which I uploaded ( www.kelmoride.com.au) It has things which I wanted to include such as, services I will provide, trip information, contact form etc.

I don't mind if the layout is completely different to my site as it was only a template that was included in the program I used. I would like the overall design to be relatively fluid, not having to back-track a lot to navigate the site.

```html
<!DOCTYPE html>
<html lang="en">
<head>
<meta charset="utf-8">
<title>Kelmo Ride Tours</title>
<link rel="stylesheet" href="https://fonts.googleapis.com/css2?family=Raleway:wght@600;700;800;900&family=Open+Sans:wght@400;600;700&display=swap">
<style>
:root{
  --orange:#e2582a;
  --orange-dark:#c9461c;
  --ink:#2b2b2b;
  --text:#6d6d6d;
  --light:#f1f1f1;
  --paper:#ffffff;
  --dark:#242424;
  --darker:#1b1b1b;
  --panel:#e9e9e9;
  --line:#d8d8d8;
}
*{box-sizing:border-box;margin:0;padding:0}
html,body{width:1200px;height:2552px;overflow:hidden}
body{font-family:"Open Sans",Arial,sans-serif;color:var(--text);background:var(--paper);position:relative}
.h-display{font-family:"Raleway",Arial,sans-serif;font-weight:900;color:var(--ink);text-transform:uppercase;letter-spacing:1px}
.btn{display:inline-block;background:var(--orange);color:#fff;font:700 13px "Open Sans",sans-serif;text-transform:uppercase;padding:10px 22px;letter-spacing:.5px}

/* header */
.site-header{position:absolute;top:0;left:0;width:1200px;height:80px;background:#fff}
.brand{position:absolute;left:130px;top:12px;display:flex;align-items:center;gap:8px;font:700 20px "Raleway",sans-serif;color:var(--ink)}
.brand-dot{width:14px;height:14px;background:var(--orange)}
.social{position:absolute;right:140px;top:18px;display:flex;gap:10px}
.social span{width:14px;height:14px;border-radius:50%;background:#555}
.nav{position:absolute;left:140px;top:48px;display:flex;gap:30px;font:600 12px "Open Sans",sans-serif;color:#444}
.nav a{color:inherit;text-decoration:none;padding-bottom:8px}
.nav a.active{color:var(--orange);border-bottom:2px solid var(--orange)}

/* hero */
.hero{position:absolute;top:80px;left:0;width:1200px;height:572px;background:linear-gradient(180deg,#c9ccd0 0%,#9ea3a8 55%,#5c5f62 100%)}
.hero-caption{position:absolute;left:140px;top:390px;width:420px}
.hero-caption h2{background:rgba(30,30,30,.85);color:#fff;font:800 15px "Raleway",sans-serif;padding:10px 14px;text-transform:uppercase}
.hero-caption p{background:rgba(255,255,255,.92);color:#333;font-size:13px;padding:10px 14px;line-height:1.5}
.hero-caption .btn{margin-top:12px}

/* newsletter */
.newsletter{position:absolute;top:652px;left:0;width:1200px;height:88px;background:var(--dark);display:flex;align-items:center;padding-left:160px;gap:22px;color:#fff}
.newsletter-label{font:600 13px "Open Sans",sans-serif;line-height:1.3;width:170px}
.field{width:200px;height:34px;background:#3a3a3a;border:1px solid #4a4a4a;color:#999;font-size:12px;padding:9px 12px}
.newsletter .btn{padding:9px 26px}

/* about */
.about{position:absolute;top:740px;left:0;width:1200px;height:292px;background:var(--light);text-align:center}
.about h2{font-size:54px;margin-top:40px}
.divider{display:block;margin:6px auto 0}
.about h3{font:600 16px "Open Sans",sans-serif;color:#444;margin-top:14px}
.about p{width:520px;margin:10px auto 0;font-size:14px;line-height:1.5}
.about .btn{margin-top:18px}

/* services */
.services{position:absolute;top:1032px;left:0;width:1200px;height:368px;background:var(--darker);text-align:center}
.services h2{font-size:54px;color:#fff;margin-top:30px}
.service-card{position:absolute;top:128px;width:420px;height:180px;background:var(--panel);text-align:left;padding:18px 22px}
.service-card h4{font:700 16px "Raleway",sans-serif;color:var(--ink)}
.service-card p{font-size:13px;line-height:1.5;margin-top:10px}
.service-card .more{position:absolute;right:20px;bottom:20px;background:#2c2c2c;color:#fff;font:700 11px "Open Sans",sans-serif;padding:7px 16px}
.arrow{position:absolute;top:200px;width:26px;height:26px;border-radius:50%;background:#444}

/* gallery */
.gallery{position:absolute;top:1400px;left:0;width:1200px;height:480px;background:#fff;text-align:center}
.gallery h2{font-size:54px;margin-top:44px}
.dots{display:flex;gap:6px;justify-content:center;margin-top:8px}
.dots span{width:8px;height:8px;border-radius:50%;background:#bbb}
.dots span.on{background:var(--orange)}
.filters{display:flex;justify-content:center;gap:6px;margin-top:40px}
.filters span{font-size:11px;background:#2c2c2c;color:#fff;padding:4px 12px}
.filters span.on{background:var(--orange)}
.shot{position:absolute;top:228px;width:288px}
.shot-img{height:172px;position:relative}
.shot-tag{position:absolute;left:0;bottom:10px;background:var(--orange);color:#fff;font:700 12px "Open Sans",sans-serif;padding:4px 10px}
.shot p{text-align:left;font-size:12px;line-height:1.45;margin-top:8px}

/* news + testimonials */
.news{position:absolute;top:1880px;left:128px;width:460px}
.col-title{font:700 20px "Raleway",sans-serif;color:var(--ink);padding-bottom:10px;border-bottom:1px solid var(--line)}
.col-title::after{content:"";display:block;width:60px;height:3px;background:var(--orange);margin-top:9px;margin-bottom:-11px}
.news-item{display:flex;gap:18px;margin-top:26px}
.news-thumb{width:130px;height:96px;flex:none}
.news-item h5{font:700 18px "Raleway",sans-serif;color:var(--orange)}
.news-item .date{font-size:11px;color:#999;margin-top:2px}
.news-item p{font-size:12px;line-height:1.5;margin-top:6px}
.testimonials{position:absolute;top:1880px;left:616px;width:456px}
.quote-box{margin-top:26px;border:1px solid var(--line);padding:26px 24px 26px 90px;position:relative;font-size:13px;line-height:1.6;height:186px}
.quote-mark{position:absolute;left:22px;top:26px;width:44px;height:44px;background:var(--orange)}
.person{display:flex;align-items:center;gap:14px;margin-top:26px}
.avatar{width:48px;height:48px;border-radius:50%;background:#c4c4c4}
.person b{font-size:13px;color:#444;display:block}
.person span{font-size:11px;color:var(--orange)}

/* footer */
.site-footer{position:absolute;top:2312px;left:0;width:1200px;height:216px;background:var(--dark);color:#aaa}
.f-col{position:absolute;top:34px}
.f-col h6{font:700 14px "Raleway",sans-serif;color:#fff;text-transform:uppercase;margin-bottom:12px}
.f-col p{font-size:12px;line-height:1.6}
.f-social{display:flex;gap:10px;margin-bottom:14px}
.f-social span{width:18px;height:18px;border-radius:50%;background:#666}
.to-top{position:absolute;right:128px;top:-2px;width:36px;height:36px;border-radius:50%;background:#3a3a3a;border:1px solid #555}
.copyright{position:absolute;top:2528px;left:0;width:1200px;height:24px;background:#141414;color:#888;font-size:11px;display:flex;justify-content:space-between;align-items:center;padding:0 128px}
</style>
</head>
<body>

<header class="site-header">
  <div class="brand"><span class="brand-dot"></span>Kelmo Ride Tours</div>
  <div class="social"><span></span><span></span><span></span><span></span><span></span><span></span></div>
  <nav class="nav">
    <a class="active">Home</a><a>About Us</a><a>Services</a><a>Trips on Offer</a><a>Book a Trip</a><a>Contact Us</a>
  </nav>
</header>

<section class="hero" role="img" aria-label="Two modern coaches parked side by side">
  <div class="hero-caption">
    <h2>Lorem ipsum is simply dummy text</h2>
    <p>Lorem Ipsum is simply dummy text of the printing and typesetting industry.</p>
    <span class="btn">Read More</span>
  </div>
</section>

<section class="newsletter">
  <svg width="36" height="30" viewBox="0 0 36 30"><path d="M2 14 34 2 26 28 16 18Z M16 18 34 2" fill="none" stroke="#fff" stroke-width="2" stroke-linejoin="round"/></svg>
  <div class="newsletter-label">Subscribe to our Newsletter</div>
  <div class="field">Enter Your Name</div>
  <div class="field">Enter Your Email</div>
  <span class="btn">Subscribe</span>
</section>

<section class="about">
  <h2 class="h-display">About Us</h2>
  <svg class="divider" width="300" height="14" viewBox="0 0 300 14"><path d="M0 7H130L140 2H160L170 7H300" fill="none" stroke="#999" stroke-width="2"/></svg>
  <h3>Welcome To Our Company</h3>
  <p>Kelmo Ride Tours is a family run business that aims to deliver great service and value for money, with bus trips and tours around Victoria and interstate.</p>
  <span class="btn">Read More</span>
</section>

<section class="services">
  <h2 class="h-display">Our Services</h2>
  <svg class="divider" width="300" height="14" viewBox="0 0 300 14"><path d="M0 7H130L140 2H160L170 7H300" fill="none" stroke="#666" stroke-width="2"/></svg>
  <span class="arrow" style="left:134px"></span>
  <div class="service-card" style="left:180px">
    <h4>Weddings</h4>
    <p>Our comfortable bus can transport your guests to the church and on to the reception. We take care of every detail so your big day runs on time and free of stress.</p>
    <span class="more">READ MORE</span>
  </div>
  <div class="service-card" style="left:640px">
    <h4>BUCK'S Party</h4>
    <p>Planning a night out with the lads? Let us do the driving while your group enjoys the trip. We pick up and drop off at any place you choose around the region.</p>
    <span class="more">READ MORE</span>
  </div>
  <span class="arrow" style="left:1040px"></span>
</section>

<section class="gallery">
  <h2 class="h-display">Picture Gallery</h2>
  <div class="dots"><span></span><span class="on"></span><span></span></div>
  <div class="filters">
    <span class="on">All</span><span>Weddings</span><span>Buck's Party</span><span>Hens Party</span><span>Birthdays</span><span>Corporate</span><span>Sporting</span><span>Mystery Trips</span>
  </div>
  <div class="shot" style="left:144px">
    <div class="shot-img" role="img" aria-label="Sports team celebrating on a field" style="background:linear-gradient(135deg,#7a2a1e,#c24a2e)"><span class="shot-tag">SPORTS</span></div>
    <p>Contrary to popular belief, Lorem Ipsum is not simply random text.</p>
  </div>
  <div class="shot" style="left:456px">
    <div class="shot-img" role="img" aria-label="White wedding flower bouquet" style="background:linear-gradient(135deg,#dfe6d4,#8aa86a)"><span class="shot-tag">WEDDING</span></div>
    <p>Contrary to popular belief, Lorem Ipsum is not simply random text.</p>
  </div>
  <div class="shot" style="left:768px">
    <div class="shot-img" role="img" aria-label="Birthday cake with candles" style="background:linear-gradient(135deg,#f1e3c8,#c89a5a)"><span class="shot-tag">BIRTHDAY</span></div>
    <p>Contrary to popular belief, Lorem Ipsum is not simply random text.</p>
  </div>
</section>

<section class="news">
  <h3 class="col-title">Latest News</h3>
  <div class="news-item">
    <div class="news-thumb" role="img" aria-label="Laptop on a desk" style="background:linear-gradient(135deg,#cfd8e3,#7d8fa6)"></div>
    <div>
      <h5>Place Your Heading</h5>
      <div class="date">September 12, 2015 · 2 Comments</div>
      <p>Lorem ipsum dolor sit amet, consectetur adipiscing elit. Integer nec odio praesent libero sed cursus ante dapibus diam.</p>
    </div>
  </div>
  <div class="news-item">
    <div class="news-thumb" role="img" aria-label="Group of travellers outdoors" style="background:linear-gradient(135deg,#d7c9b6,#8f7a62)"></div>
    <div>
      <h5>Place Your Heading</h5>
      <div class="date">September 10, 2015 · 4 Comments</div>
      <p>Lorem ipsum dolor sit amet, consectetur adipiscing elit. Integer nec odio praesent libero sed cursus ante dapibus diam.</p>
    </div>
  </div>
</section>

<section class="testimonials">
  <h3 class="col-title">Testimonials</h3>
  <div class="quote-box">
    <svg class="quote-mark" viewBox="0 0 44 44"><rect width="44" height="44" fill="#e2582a"/><path d="M12 28V20Q12 14 18 13V17Q16 18 16 21H19V28ZM25 28V20Q25 14 31 13V17Q29 18 29 21H32V28Z" fill="#fff"/></svg>
    Lorem ipsum dolor sit amet, consectetur adipiscing elit. Integer nec odio praesent libero. Sed cursus ante dapibus diam. Sed nisi, nulla quis sem at nibh elementum imperdiet. Duis sagittis ipsum praesent mauris fusce nec tellus sed augue semper porta. Mauris massa vestibulum lacinia arcu eget nulla.
  </div>
  <div class="person">
    <div class="avatar" role="img" aria-label="Customer portrait"></div>
    <div><b>Nora Pell</b><span>Trip Passenger</span></div>
  </div>
</section>

<footer class="site-footer">
  <span class="to-top"></span>
  <div class="f-col" style="left:160px;width:240px">
    <h6>About Us</h6>
    <p>Lorem ipsum dolor sit amet, consectetur adipiscing elit. Vestibulum auctor ornare leo non suscipit dapibus.</p>
    <p style="margin-top:10px">Kelmo Ride Tours<br>12 Harbour Lane<br>Geelong VIC 3220</p>
  </div>
  <div class="f-col" style="left:472px;width:260px">
    <h6>Contact Information</h6>
    <p>Company Name<br>Address 1<br>Address 2<br>Town<br>Zip Code</p>
    <p style="margin-top:8px">+61 3 5200 0000</p>
    <p>www.kelmoride.com.au</p>
  </div>
  <div class="f-col" style="left:840px;width:240px">
    <h6>Connect With Us</h6>
    <div class="f-social"><span></span><span></span><span></span><span></span><span></span><span></span></div>
    <p>Sign up to our newsletter</p>
    <div class="field" style="margin-top:8px;width:220px;height:28px;padding:6px 10px">Enter Your Email</div>
  </div>
</footer>
<div class="copyright"><span>Copyright © 2015 Kelmo Ride Tours</span><span>Powered by Kelmo</span></div>

</body>
</html>
```